AMAZING WEBSITE DESIGN NEEDED FOR MAID / CLEANING SERVICE

NOTE: This is Website Design Only - No coding required

Please submit your designs ASAP as we want to pick a winner and get started!

Hey,

We are looking for a new amazing website design for a maid or cleaning service.

They have a horrible website that we want turned into a masterpiece.

As you will see on their current site:

http://tidyharborco.examplehost.net/

They have a lot of stuff, very disorganized, and need help.

Here is what we need:

Colors: Same as current site, Orange, Gray, Black

Menu: Horizontal with same Menu items

Need a spot for a video on the homepage

Want content to be structured in a great format that is easy to read.

Want to highlight commercial and residential on the website homepage.

Also want a spot for customer testimonials

We want the site clean, professional, fresh and modern.

Please help by matching the logo design.

I look forward to your designs!
Updates

Hi All! Really appreciate your efforts and designs. I will be meeting with our client on Monday and will then be able to provide feedback after our meeting. If you have other ideas, please submit them. The more I can show him the better! Thanks!

Target Market(s)

The target market is residential home owners as well as commercial businesses who need cleaning on a regular basis.

This company cleans homes and offices for individuals.

Industry/Entity Type

Residential

Font styles to use
Sans Serif

Requirements
Must have
• Must match logo colors
Must have spot for video
Must have a clean look
Must have a bold look
Nice to have
• Highly visual
Should not have
• clutter
messy design
hard to read

```html
<!DOCTYPE html>
<html lang="en">
<head>
<meta charset="utf-8">
<title>Tidy Harbor – Quality Commercial &amp; Residential Cleaning</title>
<link rel="stylesheet" href="https://fonts.googleapis.com/css2?family=Cabin:wght@400;500;600&family=Arimo:ital,wght@0,400;0,700;1,400;1,700&display=swap">
<style>
:root{
  --orange:#e57716;
  --orange-dark:#c9600b;
  --charcoal:#3d3d3d;
  --nav-top:#5a5a5a;
  --nav-bottom:#3a3a3a;
  --text:#2b2b2b;
  --heading:#4a4a4a;
  --header-bg:#f2f2f2;
  --rule:#d9d9d9;
  --white:#ffffff;
}
*{box-sizing:border-box;margin:0;padding:0}
html,body{width:1065px;height:1200px;overflow:hidden;background:var(--white)}
.stage{position:relative;width:1200px;height:1351px;transform:scale(.8875);transform-origin:0 0;font-family:"Arimo",Arial,sans-serif;color:var(--text)}
.page{position:absolute;left:102px;top:0;width:996px;height:1351px;background:var(--white);box-shadow:0 0 4px rgba(0,0,0,.12)}
.abs{position:absolute}

/* header */
.site-header{left:0;top:0;width:996px;height:133px;background:var(--header-bg);border-top:3px solid var(--orange)}
.brand{left:26px;top:70px;display:flex;align-items:center;gap:10px}
.brand-mark{width:30px;height:30px;background:var(--orange)}
.brand-name{font-family:"Cabin",sans-serif;font-weight:600;font-size:32px;color:var(--charcoal);letter-spacing:-.5px}
.brand-tagline{left:66px;top:110px;font-size:11.5px;font-style:italic;font-weight:700;color:#666}
.social{right:40px;top:34px;display:flex;gap:6px}
.social span{width:28px;height:28px;border-radius:5px;background:var(--orange);box-shadow:inset 0 -6px 8px rgba(0,0,0,.12)}
.social span:nth-child(3){background:#4aa6d9}
.social span:nth-child(4){background:#3b5b9a}
.search{left:809px;top:92px;width:130px;height:22px;background:var(--white);border:1px solid #ddd;font-size:12px;color:#888;padding:3px 0 0 26px}
.search-badge{left:937px;top:84px;width:38px;height:38px;border-radius:50%;background:#4b4b4b}

/* nav */
.main-nav{left:0;top:133px;width:996px;height:35px;background:linear-gradient(var(--nav-top),var(--nav-bottom));display:flex}
.main-nav a{font-family:"Cabin",sans-serif;font-size:14px;color:var(--white);text-decoration:none;line-height:35px;padding:0 18px;border-right:1px solid #2a2a2a;box-shadow:1px 0 0 #6a6a6a}
.main-nav a.active{background:var(--orange);padding:0 14px 0 25px}

/* hero */
.hero{left:0;top:169px;width:995px;height:382px;background:linear-gradient(90deg,#dcd9d2 0%,#e8dccf 35%,#c7a383 55%,#e9e4dc 80%,#eeeae4 100%)}
.hero-thumb{width:172px;height:102px;border:2px solid #fff;box-shadow:2px 2px 6px rgba(0,0,0,.35)}
.hero-caption{left:0;top:321px;width:576px;height:45px;background:rgba(40,40,40,.75);color:var(--white);font-family:"Cabin",sans-serif;font-size:23px;line-height:45px;padding-left:10px;letter-spacing:.5px}

/* sections */
.section-title{font-family:"Cabin",sans-serif;font-weight:400;font-size:31px;color:var(--heading);letter-spacing:.5px}
.section-title b{font-weight:600}
.section-title em{font-style:normal;color:var(--orange)}
.copy{font-size:14.2px;line-height:20px;color:var(--text)}
.btn{display:inline-block;background:var(--charcoal);color:var(--white);font-family:"Cabin",sans-serif;font-size:14.5px;border-radius:7px;padding:6px 8px;box-shadow:0 1px 2px rgba(0,0,0,.4)}

.welcome-photo{left:-17px;top:560px;width:200px;height:368px;border-radius:100px 100px 20px 20px;background:linear-gradient(#e8c48a,#f1e36a 55%,#f6f1d2)}
.ticks{list-style:none}
.ticks li{position:relative;padding-left:32px;height:28px;font-size:14.2px}
.ticks svg{position:absolute;left:0;top:-3px}
.video{left:698px;top:644px;width:281px;height:150px;background:linear-gradient(#3b3f44,#777c80 60%,#2a2a2a);border:1px solid #ccc}
.video-label{left:6px;top:4px;font-size:6px;color:#ddd}
.video-bar{left:0;bottom:0;width:100%;height:14px;background:#1d1d1d}
.testimonial-frame{left:697px;top:984px;width:283px;height:157px;border:1px solid #ccc;padding:4px;background:#fff}
.testimonial-photo{width:100%;height:100%;background:linear-gradient(135deg,#cfd6d8,#e9c94a 40%,#d84f8b 60%,#c7dfe6)}
.quote-badge{left:798px;top:1101px;width:64px;height:64px;border-radius:50%;background:var(--orange);color:#3a2a1a;font-family:Georgia,serif;font-size:74px;font-weight:700;text-align:center;line-height:86px}
.quote{left:690px;top:1174px;width:300px;text-align:center;font-style:italic;font-size:14.2px;line-height:20px}
.quote-name{left:690px;top:1240px;width:300px;text-align:center;font-style:italic;font-weight:700;font-size:12px}

/* footer */
.site-footer{left:0;top:1267px;width:996px;height:84px;background:linear-gradient(#666,#3c3c3c);color:var(--white);font-family:"Cabin",sans-serif;font-size:14px;text-align:center}
.footer-nav{padding-top:20px;word-spacing:2px}
.footer-nav span{margin:0 9px}
.copyright{margin-top:20px}
</style>
</head>
<body>
<div class="stage">
 <div class="page">
  <header class="abs site-header">
   <div class="abs brand"><span class="brand-mark"></span><span class="brand-name">Tidy Harbor</span></div>
   <div class="abs brand-tagline">Quality Commercial &amp; Residential Cleaning</div>
   <div class="abs social"><span></span><span></span><span></span><span></span></div>
   <div class="abs search">Search here ...</div>
   <div class="abs search-badge" role="img" aria-label="Mascot beside search field"></div>
  </header>

  <nav class="abs main-nav">
   <a class="active">Home</a><a>Our Services</a><a>Our Employees</a><a>Why Choose Us?</a><a>Testimonials</a><a>Special Offers</a><a>About Us</a><a>Contact Us</a><a>Request a Bid</a>
  </nav>

  <section class="abs hero" role="img" aria-label="Bright, tidy living room with sofa, lamp and patio doors">
   <div class="abs hero-thumb" style="left:801px;top:17px;background:linear-gradient(135deg,#6fa8d6,#f0d9a0)" role="img" aria-label="Cleaner wiping a window"></div>
   <div class="abs hero-thumb" style="left:801px;top:143px;background:linear-gradient(135deg,#c98a4a,#4a8ed0)" role="img" aria-label="Cleaner dusting a kitchen counter"></div>
   <div class="abs hero-thumb" style="left:801px;top:267px;background:linear-gradient(135deg,#eef0e6,#4c7fc0)" role="img" aria-label="Hand with cloth cleaning a window"></div>
   <div class="abs hero-caption">Tidy Harbor – “ The new meaning to cleaning ”</div>
  </section>

  <div class="abs welcome-photo" role="img" aria-label="Smiling cleaner in yellow shirt and gloves wiping a surface"></div>
  <h2 class="abs section-title" style="left:197px;top:584px">Welcome to <b>Tidy Harbor</b></h2>
  <div class="abs" style="left:201px;top:638px;width:462px">
   <p class="copy">This is a company designed around the customer! We will make sure that you are accomodated in every way possible. It is our commitment to ensure that you have a clean, calm, and comfortable environmenta-so you can relax, live, and work with a piece of mind. We will workvery hard to make sure you experience the 'wow" factor when working with us! We truly are the new meaning of cleaning!</p>
   <p class="copy" style="margin-top:17px">Thank you for visiting us! You are one step closer to experiencing first class maid service! Our company specializes in detailed housekeep-ing, janitorial, and commerical cleaning services making your environ-ment shine and sparkle like it never has before!</p>
  </div>
  <span class="abs btn" style="left:200px;top:880px">Read more [+]</span>

  <h2 class="abs section-title" style="left:696px;top:584px"><b>Video</b> <em>Premiere</em></h2>
  <div class="abs video" role="img" aria-label="Video player showing a small dog on a carpet">
   <span class="abs video-label">Pet Clip</span>
   <svg class="abs" style="left:122px;top:63px" width="36" height="22" viewBox="0 0 36 22"><rect width="36" height="22" rx="5" fill="#1d1d1d" fill-opacity=".85"/><path d="M14 6l9 5-9 5z" fill="#fff"/></svg>
   <div class="abs video-bar"></div>
  </div>
  <p class="abs copy" style="left:699px;top:813px;width:298px">This is a company designed around the cus-tomer! We will make sure that you are acco-modated in every way possible. It is our com-mitment to ensure that [ more + ]</p>

  <h2 class="abs section-title" style="left:9px;top:937px">Why Choose <b>Tidy Harbor</b>?</h2>
  <p class="abs copy" style="left:9px;top:993px;width:660px">Thank you for visiting us! You are one step closer to experiencing first class maid service! Our company specializes in detailed housekeeping, janitorial, and commerical cleaning services making your environment shine and sparkle like it never has before!</p>
  <ul class="abs ticks" style="left:11px;top:1072px">
   <li><svg width="22" height="20" viewBox="0 0 22 20"><rect x="1" y="5" width="14" height="13" fill="none" stroke="#e57716" stroke-width="2"/><path d="M4 10l4 4 12-12" fill="none" stroke="#e57716" stroke-width="3"/></svg>We clean and scrub ovens until they shine with perfection!</li>
   <li><svg width="22" height="20" viewBox="0 0 22 20"><rect x="1" y="5" width="14" height="13" fill="none" stroke="#e57716" stroke-width="2"/><path d="M4 10l4 4 12-12" fill="none" stroke="#e57716" stroke-width="3"/></svg>We wash, dry, iron, and hang/fold all of your laundry!</li>
   <li><svg width="22" height="20" viewBox="0 0 22 20"><rect x="1" y="5" width="14" height="13" fill="none" stroke="#e57716" stroke-width="2"/><path d="M4 10l4 4 12-12" fill="none" stroke="#e57716" stroke-width="3"/></svg>Have a cluttered room you've been meaning to get to? No worries....ask and you shall recieve!</li>
   <li><svg width="22" height="20" viewBox="0 0 22 20"><rect x="1" y="5" width="14" height="13" fill="none" stroke="#e57716" stroke-width="2"/><path d="M4 10l4 4 12-12" fill="none" stroke="#e57716" stroke-width="3"/></svg>Tidy Harbor will have it looking spectacular!</li>
   <li><svg width="22" height="20" viewBox="0 0 22 20"><rect x="1" y="5" width="14" height="13" fill="none" stroke="#e57716" stroke-width="2"/><path d="M4 10l4 4 12-12" fill="none" stroke="#e57716" stroke-width="3"/></svg>Have a dirty pet? Have a filthy car??</li>
  </ul>
  <span class="abs btn" style="left:13px;top:1224px">Read more [+]</span>

  <h2 class="abs section-title" style="left:696px;top:937px">Testimonial</h2>
  <div class="abs testimonial-frame"><div class="testimonial-photo" role="img" aria-label="Person in yellow gloves holding cleaning supplies"></div></div>
  <div class="abs quote-badge">“</div>
  <p class="abs quote">“This is a company designed around the cus-tomer! We will make sure that you are acco-modated in every way possible. ”</p>
  <p class="abs quote-name">Lena Castro 29 Years</p>

  <footer class="abs site-footer">
   <div class="footer-nav">Home<span>~</span>Our Services<span>~</span>Our Employees<span>~</span>Why Choose Us?<span>~</span>Testimonials<span>~</span>About Us<span>~</span>Contact Us</div>
   <div class="copyright">Copyright @ Tidy Harbor. All Right Reserved</div>
  </footer>
 </div>
</div>
</body>
</html>
```